Talvane Salmon Labels

We need a graphic design label for a new product launch. Talvane is an 100% Australian family business specialised in making marinades made from natural and locally sourced fresh ingredients for fish and seafood. We make remarkable food for fine cooking prepared by hand at our kitchen in Condell Park, using the same ingredients and techniques you would use at home.

We are planning to launch three marinades for salmon.
The flavours are:

- Herb, Lemon & Cracked Black Pepper
- Ginger, Honey & Soy
- Coriander, Lemongrass, Shallot and Ginger

The marinades will be packed in a 300 grams clear pouch with spout and sold in the seafood section of a major retail supermarket.

Measurements of the pouch: 140 mm wide and 210 mm high but only 160 mm high from the spout downwards.

Label: For the label, It will be a 120mm wide X 120mm high If not slightly smaller. Please refer to File 2: to see the pouch.

The label will cover 75% of the front of the pouch and the marinade itself will be visible in the remaining 25 % of the pouch. The colours of the marinades are green for Herb, Lemon & Cracked Black Pepper and Coriander, Lemongrass, Shallot and Ginger; and dark brown for Ginger, Honey & Soy.

Our marinades do not contain additives. The marinades are Gluten free.

The label needs to visually communicate that the marinade is used for salmon.

Please choose a suitable typography for our name Talvane that communicates an artisan feel.

Please refer to File 1 as a guide to what we would like, but keep in mind we are very open to any ideas you may have.

Colours should reflect the nature of our business, as outlined above.
Updates

Hello Designers,

This is what the actual pouch looks like https://www.filecrate.example/sc/4kd82mz19qp0x/Tq73Lowm8_

We would like the label to be roughly 120mm X 120mm or within those parameters to fit the packaging.

Thank you!
- Miriam

Hey Designers,

we have been looking at your designs and while we have liked some elements of them we would like to see more creativity with the actual graphics and shapes of the labels, different colour contrast and more clever and quirky designs. We want to make fish fun and interesting to consumers, something rustic that catches the eye but at the same time is still sophisticated and upmarket. 

We would like to see the following on your packaging designs:

- Pastels colours (green, blue and yellow).
- The 'Talvane gourmet' font to be in bolder typography
- An ink looking stamp for 'gluten free, no additives'
- Something about the product being hand crafted
- Must include the following text: Marinades made from natural and locally sourced fresh ingredients for fish and seafood

here are some examples for you to be inspired by

Some font ideas ..

http://pinboardly.example/pin/501928374650192837/
http://pinboardly.example/pin/73019284756102938/
http://pinboardly.example/pin/618293047561829304/
http://pinboardly.example/pin/339201847562019384/
http://pinboardly.example/pin/447102938475610293/
http://pinboardly.example/pin/582019374651029384/

colours/images/graphics

http://pinboardly.example/pin/194820375619203847/
http://pinboardly.example/pin/730192846501928374/
http://pinboardly.example/pin/865019283746501927/
http://pinboardly.example/pin/412093847561029384/ (We like this concept) 

Good luck! 

 

Target Market(s)

Home cooks, young professionals, anyone with a healthy eating lifestyle.

Industry/Entity Type

Graphic Design

Requirements
Must have
• The label needs to visually communicate that the marinade is used for salmon.
- Include "Gluten Free" and "No Additives" on the label
- Outline the freshness of the ingredients used in the marinade eg. Coriander, Lemongrass, Shallot and Ginger to be included on the label.
- Bright and eye catching colours (food friendly colours).
Nice to have
• - Open to pastel colours
- Vector drawings
Should not have
• - dull colours

```html
<!DOCTYPE html>
<html lang="en">
<head>
<meta charset="utf-8">
<title>Talvane Salmon Marinade Label</title>
<link rel="stylesheet" href="https://fonts.googleapis.com/css2?family=Oswald:wght@400&family=Fondamento&family=Parisienne&family=Poiret+One&display=swap">
<style>
  :root {
    --page: #ffffff;
    --teal: #35bfb8;
    --frame-yellow: #f3ec47;
    --brand-blue: #2c3a9c;
    --accent-red: #d3283f;
    --herb-green: #1f7a4d;
    --fresh-green: #1f9a45;
  }
  html, body {
    margin: 0;
    padding: 0;
    width: 1200px;
    height: 1200px;
    overflow: hidden;
    background: var(--page);
  }
  .label {
    position: absolute;
    left: 72px;
    top: 78px;
    width: 1056px;
    height: 1040px;
    background: var(--teal);
  }
  .frame {
    position: absolute;
    left: 0;
    top: 0;
    width: 1200px;
    height: 1200px;
  }
  .brand-name {
    position: absolute;
    left: 0;
    width: 1200px;
    top: 320px;
    margin: 0;
    text-align: center;
    font-family: "Oswald", sans-serif;
    font-weight: 400;
    font-size: 140px;
    line-height: 1;
    letter-spacing: 2px;
    color: var(--brand-blue);
  }
  .product-name {
    position: absolute;
    left: 0;
    width: 1200px;
    top: 505px;
    margin: 0;
    text-align: center;
    font-family: "Fondamento", cursive;
    font-weight: 400;
    font-size: 70px;
    line-height: 1;
    letter-spacing: 3px;
    color: var(--accent-red);
  }
  .flavour {
    position: absolute;
    left: 0;
    width: 1200px;
    top: 600px;
    margin: 0;
    text-align: center;
    font-family: "Parisienne", cursive;
    font-size: 38px;
    line-height: 1;
    color: var(--herb-green);
  }
  .salmon-art {
    position: absolute;
    left: 308px;
    top: 683px;
    width: 570px;
    height: 157px;
    border-radius: 80px 30px 30px 80px;
    background: var(--frame-yellow);
  }
  .claims {
    position: absolute;
    left: 208px;
    top: 918px;
    margin: 0;
    padding: 0;
    list-style: none;
    font-family: "Poiret One", sans-serif;
    font-size: 25px;
    color: var(--accent-red);
  }
  .claims li {
    display: flex;
    align-items: center;
    height: 48px;
  }
  .claims svg {
    width: 30px;
    height: 30px;
    margin-right: 14px;
  }
  .fresh-tag {
    position: absolute;
    left: 770px;
    top: 950px;
    margin: 0;
    font-family: "Fondamento", cursive;
    font-size: 60px;
    line-height: 1;
    letter-spacing: 2px;
    color: var(--fresh-green);
  }
</style>
</head>
<body>
  <div class="label"></div>

  <svg class="frame" viewBox="0 0 1200 1200" fill="none" stroke="var(--frame-yellow)" stroke-width="7" stroke-linecap="round">
    <path d="M140 135 Q600 200 1060 135" />
    <path d="M150 1050 Q600 1000 1050 1060" />
    <path d="M128 150 Q160 600 135 1020" />
    <path d="M1072 150 Q1040 600 1068 1030" />
    <ellipse cx="108" cy="115" rx="26" ry="24" />
    <ellipse cx="1090" cy="115" rx="26" ry="24" />
    <ellipse cx="118" cy="1040" rx="26" ry="24" />
    <ellipse cx="1075" cy="1055" rx="26" ry="24" />
  </svg>

  <h1 class="brand-name">TALVANE</h1>
  <h2 class="product-name">salmon marinade</h2>
  <p class="flavour">Herb, Lemon &amp; Cracked Black Pepper</p>

  <div class="salmon-art" role="img" aria-label="Engraved-style yellow salmon illustration"></div>

  <ul class="claims">
    <li>
      <svg viewBox="0 0 30 30" fill="none" stroke="var(--accent-red)" stroke-width="3" stroke-linecap="round"><path d="M4 17 L11 25 L26 5" /></svg>
      Gluten Free
    </li>
    <li>
      <svg viewBox="0 0 30 30" fill="none" stroke="var(--accent-red)" stroke-width="3" stroke-linecap="round"><path d="M4 17 L11 25 L26 5" /></svg>
      No Additives
    </li>
  </ul>

  <p class="fresh-tag">fresh</p>
</body>
</html>
```